Crestline Productions Business Logo and Card Design

PLEASE LIMIT your submission to maximum of 2 at a time.
Crestline Productions provides video production services, and produces videos, that help people connect in the spirit of unity and peace.Primarily I am looking for a logo that is simple to remember but the concept is fairly complex. The concept of the logo is a peace dove with an olive branch in it's mouth has it's wings around earth, symbolising that it is protecting earth with peace. If possible I'd like this logo done and delivered in high quality vector format, so I can use it for banners etc.Then the business card I just want a simple white card with the logo in the middle and contact info under the logo. Open to suggestions if you think there should be anything else included, but it must remain simple and uncluttered. Also incorporate something in the logo that says film and video e.g.: film strip or camera lens

Industry/Entity Type

Business

Contact Information for Business Card

Crestline Productions
www.crestline.example
darveen@crestline.example
+61 455 118 207

Requirements
Must have
• Logo must have the following:
• Peace Dove
• Olive branch
• Earth
• Something about video production (e.g.: film strip or camera lens or anything film related)

```html
<!DOCTYPE html>
<html lang="en">
<head>
<meta charset="utf-8">
<title>Crestline Productions Business Card</title>
<link rel="stylesheet" href="https://fonts.googleapis.com/css2?family=Exo+2:wght@500;600&display=swap">
<style>
  :root {
    --backdrop: #1d1d1d;
    --card-dark: #333333;
    --card-mid: #3c3c3c;
    --card-edge: #4a4a4a;
    --brand-green: #12a74b;
    --brand-blue: #2f6fb6;
  }
  * { box-sizing: border-box; margin: 0; padding: 0; }
  html, body {
    width: 1200px;
    height: 902px;
    overflow: hidden;
    background: var(--backdrop);
    font-family: "Exo 2", sans-serif;
  }
  .canvas {
    position: relative;
    width: 1200px;
    height: 902px;
  }
  .business-card {
    position: absolute;
    left: 383px;
    top: 71px;
    width: 434px;
    height: 760px;
    border-radius: 6px;
    background: linear-gradient(90deg, var(--card-mid) 0%, var(--card-dark) 45%, var(--card-dark) 70%, var(--card-edge) 100%);
    box-shadow: inset 0 0 0 1px rgba(255,255,255,0.08);
    text-align: center;
  }
  .brand {
    position: absolute;
    top: 62px;
    left: 0;
    right: 0;
    display: flex;
    flex-direction: column;
    align-items: center;
  }
  .brand-mark {
    width: 150px;
    height: 150px;
  }
  .brand-name {
    margin-top: 22px;
    color: var(--brand-green);
    font-weight: 600;
    font-size: 34px;
    line-height: 1.1;
    letter-spacing: 2px;
    text-transform: uppercase;
  }
  .person {
    position: absolute;
    top: 372px;
    left: 0;
    right: 0;
  }
  .person-name {
    color: var(--brand-green);
    font-weight: 600;
    font-size: 34px;
    line-height: 1;
  }
  .person-role {
    margin-top: 6px;
    color: var(--brand-blue);
    font-weight: 500;
    font-size: 22px;
  }
  .contact {
    position: absolute;
    top: 540px;
    left: 0;
    right: 0;
    color: var(--brand-blue);
    font-weight: 500;
  }
  .contact-phone {
    font-size: 33px;
    line-height: 1.1;
  }
  .contact-email,
  .contact-web {
    font-size: 21px;
    line-height: 1.2;
  }
  .contact-email { margin-top: 10px; }
  .contact-web { margin-top: 13px; }
</style>
</head>
<body>
<main class="canvas">
  <section class="business-card">
    <div class="brand">
      <svg class="brand-mark" viewBox="0 0 150 150" aria-hidden="true">
        <circle cx="75" cy="75" r="72" fill="var(--brand-blue)"/>
      </svg>
      <p class="brand-name">Crestline<br>Productions</p>
    </div>

    <div class="person">
      <h1 class="person-name">EMPLOYEE NAME</h1>
      <p class="person-role">Managing Director</p>
    </div>

    <div class="contact">
      <p class="contact-phone">+61 455 118 207</p>
      <p class="contact-email">darveen@crestline.example</p>
      <p class="contact-web">www.crestline.example</p>
    </div>
  </section>
</main>
</body>
</html>
```